Calloway Aeronautics website

We are an aviation company based in Bayview Shores, FL but with worldwide coverage. We are involved in commercial aircraft (mostly freighters) trading, sale & leasing. Specifically, we specialized in freighters of the Vantrex family (V310, V320, V330, V340, V350). We also assist with financing, sale/leaseback. Handle special aviation projects and provide consultancy services. Currently engaged in a Vantrex 350 passenger to Freighter conversion (P2F).

Website Preliminary Initial Content/Sections as follows:

About Us
Founded in 2011, Calloway Aeronautics' management has many years of experience in Aviation, a strong background in scheduled airlines with emphasis in all cargo operations, freight forwarding supply chain and freight logistics, as well as ACMI and CMI operations.

Calloway’s focuses in facilitating wet and dry lease operations, charter and ACMI programs consultancy, aircraft sales, leasing and procurement, aviation consultancy and aircraft management.

Calloway team is a hands-on reliable alternative that works toward achieving your aircraft and aviation objectives by meeting your requirements and timeframe throughout professional and personalized service.

Teodoro Lasalle has over three decades of experience in the aviation field including aircraft maintenance, airline management, supply chain and logistics management. Teodoro is a true entrepreneur with proven experience and expertise on the multiple facets of the commercial aviation industry throughout the creation and development of a cluster of aviation entities. Teodoro is the founder and former sole member/chairman of 64 Jet, a Vantrex 340 All-Cargo U.S. Certificated Air Carrier created from scratch in 2014 which nowadays conforms a superb growing airline platform with an immaculate compliance operational record.

Services

Aircraft Finance, Trading, Procurement and Leasing
Calloway buys, sells, leases and facilitates aircraft trading while specializes in structured aircraft investment projects. Calloway has deep industry relationships and years of expertise, allowing to successfully execute lease transactions. We assist airlines, financial institutions and leasing companies when selling or purchasing aircraft.

Aircraft Available for Sale/Lease

Sale/Leaseback
Sale-leaseback is a method of financing. If your company needs liquidity, your aircraft or engine can serve as collateral for a loan throughout a sale-leaseback transaction. Sale-leaseback can free the equity tied up in aircraft or asset. Even if there is no pressing need for funds, a sale-leaseback allows you to use the equity tied up in your aircraft in a more productive fashion. Leaseback arrangements are usually employed because they confer financing, accounting or taxation benefits.

Passenger to Freighter Conversion (P2F)
Pandemic has seen the resurgence of operators packing freight into the main cabins of passenger aircraft. Carriers have been allowed to transport cargo in the cabin by removing passenger seats completely. NCA/ORSA have established exemptions that allow operators to fly in “Preighter” configuration for a limited time. Calloway is closely working with a U.S. group that is developing a Class E Supplemental Type Certificate (STC) for applicability on V350 aircraft which will include a cargo door for containerized freight. Final approvals are expected during first quarter of 2022.
Wet lease
Throughout our deep relationships within the industry, Calloway facilitates short or long-term wet leases to airlines and qualified parties around the globe, whereby we provide the Aircraft, Crews, Maintenance and Insurance (ACMI) worldwide services at competitive rates. We also specialize in AM leases where the aircraft is registered onto Lessee´s AOC with all maintenance services included in the rates, covering all maintenance risks, or CM or CMI where the client provides the aircraft.

Dry Lease
We offer aircraft from our own portfolio on dry lease or could engage in procuring the aircraft of your choice.

Asset & Aircraft Management
We provide aircraft owners Aircraft Management services, where we manage the technical side of the aircraft or the asset. Calloway also provides Harwick Dynamo engines trading, repair and full management services. We also buy Vantrex/Skylane surplus inventory.

Worldwide Charters
We facilitate the arrangement of full charters to airlines and logistics companies. Certain territory restrictions may apply.

Aviation Consultancy
We provide airline consultancy services for new or special projects. Calloway also specializes on All Cargo International route analysis, implementation and development. Our team provides professional guidance in obtaining worldwide both scheduled and charter authority.

Target Market(s)

Our target market are the airlines, logistics companies and commercial aviation related entities

Industry/Entity Type

Commercial Aviation

Coding

Number of Pages Required

3 page

Requirements
Must have
• Illustrations of wide body freighters such V350, V340, V320

```html
<!DOCTYPE html>
<html lang="en">
<head>
<meta charset="utf-8">
<title>Calloway Aeronautics — Website Design</title>
<link href="https://fonts.googleapis.com/css2?family=Raleway:wght@400;500;600;700&family=Tenor+Sans&display=swap" rel="stylesheet">
<style>
:root{
  --navy:#001c3b;
  --navy-deep:#000d2a;
  --mist:#bdc8ce;
  --paper:#f7f7f7;
  --board:#d9dee6;
  --slate:#98adc4;
  --ink:#3a4556;
  --muted:#7d8896;
  --white:#ffffff;
}
*{margin:0;padding:0;box-sizing:border-box}
html,body{width:1200px;height:3735px;overflow:hidden}
body{background:var(--board);font-family:'Raleway',sans-serif;color:var(--ink);position:relative}

/* style guide header */
.guide{position:absolute;left:0;top:0;width:1200px;height:300px}
.guide-logo{position:absolute;left:273px;top:176px;text-align:center;width:196px;font-family:'Tenor Sans',sans-serif;color:var(--navy)}
.guide-logo .name{font-size:29px;letter-spacing:0.5px;line-height:1;white-space:nowrap}
.guide-logo .sub{font-size:11px;letter-spacing:7px;margin-top:7px;white-space:nowrap}
.guide-rule{position:absolute;top:164px;width:1px;height:80px;background:#aab3c0}
.guide-label{position:absolute;font-family:'Tenor Sans',sans-serif;font-size:22px;color:var(--navy)}
.guide-font{position:absolute;left:577px;font-family:'Tenor Sans',sans-serif;font-size:17px;color:#6e7785}
.guide-font.raleway{font-family:'Raleway',sans-serif;font-size:16px}
.swatch{position:absolute;top:195px;width:34px;height:34px;border-radius:50%}
.swatch-code{position:absolute;top:238px;font-size:8px;color:#6e7785;width:40px;text-align:center}

/* page */
.page{position:absolute;left:238px;top:890px;width:725px;height:2750px;background:var(--white);box-shadow:0 6px 30px rgba(0,20,50,.12);overflow:hidden}
section,header,footer,.topbar{position:relative;width:725px}
.topbar{height:22px;background:var(--mist);font-size:6px;color:var(--navy)}
.topbar .contact{position:absolute;left:142px;top:7px;display:flex;gap:12px}
.topbar svg{vertical-align:-1px;margin-right:3px}
.social{position:absolute;display:flex;gap:3px}
.social span{width:8px;height:8px;border-radius:50%;background:var(--navy);display:block}
.topbar .social{left:550px;top:7px}

.nav{height:54px;background:var(--navy)}
.brand{position:absolute;left:142px;top:13px;font-family:'Tenor Sans',sans-serif;color:var(--white);text-align:center}
.brand .name{font-size:14px;line-height:1;white-space:nowrap}
.brand .sub{font-size:5px;letter-spacing:3.4px;margin-top:3px;white-space:nowrap}
.menu{position:absolute;left:318px;top:24px;display:flex;font-size:6px;font-weight:600;color:var(--white);letter-spacing:.3px;white-space:nowrap}
.menu span{padding:0 8px;border-right:1px solid rgba(255,255,255,.35)}
.menu span:last-child{border:none}
.call-btn{position:absolute;left:520px;top:17px;width:62px;height:20px;background:var(--mist);color:var(--white);font-size:5.5px;font-weight:600;display:flex;align-items:center;justify-content:center;white-space:nowrap}

.hero{height:425px}
.hero-photo{position:absolute;left:0;top:0;width:725px;height:391px;background:linear-gradient(160deg,#c9d3df 0%,#8fa2bc 35%,#4f6a96 65%,#2e4a7a 100%)}
.hero-box{position:absolute;left:142px;top:68px;width:442px;height:275px;background:rgba(120,132,160,.72);text-align:center;color:var(--white)}
.hero-box h1{font-family:'Tenor Sans',sans-serif;font-weight:400;font-size:28px;line-height:38px;margin-top:44px;white-space:nowrap}
.hero-box p{font-size:8px;line-height:14px;width:380px;margin:14px auto 0}
.tagline{position:absolute;left:0;top:343px;width:585px;height:82px;background:var(--mist)}
.tagline p{position:absolute;left:142px;top:35px;font-family:'Tenor Sans',sans-serif;font-size:11px;color:#2c3a52}

.eyebrow{position:absolute;font-size:5.5px;letter-spacing:1.5px;color:#a0a9b4}
.heading{position:absolute;font-family:'Tenor Sans',sans-serif;font-weight:400;font-size:19px;color:var(--navy)}
.center{left:0;width:725px;text-align:center}

.about{height:287px}
.about-copy{position:absolute;left:142px;top:101px;width:142px;font-size:6.5px;line-height:12.8px;color:#5d6775}
.learn-btn{position:absolute;left:142px;top:215px;width:67px;height:25px;background:#a9b6c0;color:var(--white);font-size:6px;font-weight:600;display:flex;align-items:center;justify-content:center}
.play{position:absolute;left:219px;top:213px;width:28px;height:28px;border-radius:50%;background:var(--navy);display:flex;align-items:center;justify-content:center}
.about-photo{position:absolute;left:288px;top:46px;width:145px;height:196px;background:linear-gradient(180deg,#dfe4ea,#9aa9bb 60%,#3c4d66)}
.quote{position:absolute;left:443px;top:46px;width:141px;height:196px;background:var(--navy);color:var(--white)}
.quote p{position:absolute;left:16px;top:64px;width:110px;font-size:6.2px;line-height:12.6px}
.quote svg{position:absolute;left:16px;top:30px}

.services{height:431px;background:var(--mist)}
.service{position:absolute;width:141px;height:108px}
.service .photo{width:141px;height:97px}
.service .label{position:absolute;left:7px;top:83px;width:126px;height:25px;background:var(--navy);color:var(--white);font-size:6px;display:flex;align-items:center;justify-content:center;gap:8px}
.service .label.active{background:var(--mist);color:var(--navy);border:1px solid #9aa8b3}
.dot-arrow{width:8px;height:8px;border-radius:50%;background:currentColor;display:inline-flex;align-items:center;justify-content:center}
.all-link{position:absolute;left:0;width:725px;top:384px;text-align:center;font-size:5.5px;color:var(--navy)}

.stats{height:141px;background:var(--navy);color:var(--white)}
.stat{position:absolute;top:45px;width:120px;text-align:center}
.stat b{display:block;font-family:'Tenor Sans',sans-serif;font-weight:400;font-size:21px;line-height:24px}
.stat span{font-size:6px;color:#c3ccd8}

.faq{height:345px}
.faq-col{position:absolute;top:116px;width:210px}
.faq-q{height:24px;background:var(--navy);color:var(--white);font-size:5.8px;font-weight:600;display:flex;align-items:center;justify-content:space-between;padding:0 9px;margin-bottom:5px}
.faq-q i{font-style:normal;font-size:10px;font-weight:400}
.faq-a{border:1px solid #dde2e8;border-top:none;margin:-5px 0 5px;padding:9px 9px 10px;font-size:5.8px;line-height:11px;color:#6f7884}

.banner{height:282px;background:linear-gradient(180deg,#a4b6ca,#8ea4bd)}
.banner svg.cut{position:absolute;left:0;top:0}
.plane{position:absolute;left:142px;top:0;width:442px;height:120px;background:radial-gradient(ellipse at 50% 60%,rgba(235,240,246,.55),rgba(235,240,246,0) 70%)}
.banner h2{position:absolute;top:137px;font-family:'Tenor Sans',sans-serif;font-weight:400;font-size:27px;color:var(--white);letter-spacing:.5px}
.banner p{position:absolute;top:187px;font-size:7px;color:#eef2f6}
.quote-btn{position:absolute;left:323px;top:212px;width:78px;height:25px;background:var(--navy);color:var(--white);font-size:5.5px;display:flex;align-items:center;justify-content:center}

.filler{height:264px;background:linear-gradient(90deg,var(--navy) 0%,var(--navy) 66%,var(--navy-deep) 66%)}
.filler h3{position:absolute;left:142px;top:62px;font-family:'Tenor Sans',sans-serif;font-weight:400;font-size:19px;color:var(--white)}
.filler p{position:absolute;left:142px;top:105px;width:176px;font-size:6.3px;line-height:12.4px;color:#d5dce6}
.ticks{position:absolute;left:142px;top:187px;display:flex;gap:12px;font-size:5.5px;color:#d5dce6}
.ticks svg{vertical-align:-1px;margin-right:3px}
.filler-photo{position:absolute;left:410px;top:45px;width:174px;height:174px;background:linear-gradient(180deg,#5d7395,#b8c4d3 55%,#e8edf2);border:2px solid #d0d7e0}

.testimonials{height:294px}
.avatar{position:absolute;top:91px;width:46px;height:46px;border-radius:50%;background:linear-gradient(180deg,#c9b6a6,#8c7b6e);border:2px solid #e3e6ea}
.testi{position:absolute;top:164px;width:180px;text-align:center;font-size:5.6px;line-height:10.5px;color:#7d8896}
.testi b{display:block;margin-top:14px;font-size:6.5px;font-weight:700;color:var(--navy);letter-spacing:.3px}
.testi small{display:block;font-size:5px;color:#a9b1bb}
.arrow-nav{position:absolute;top:142px;color:#98a3b0;font-size:14px}
.pager{position:absolute;top:240px;left:352px;display:flex;gap:5px}
.pager span{width:4px;height:4px;border-radius:50%;background:#c3cad2}
.pager span.on{background:var(--navy)}

.site-footer{height:184px;background:var(--mist)}
.foot-col{position:absolute;top:48px}
.foot-col h4{font-family:'Tenor Sans',sans-serif;font-weight:400;font-size:12px;color:#2c3a52;margin-bottom:13px}
.foot-col p,.foot-col li{font-size:5.2px;line-height:10px;color:#6c7786;list-style:none}
.site-footer .social{left:142px;top:125px;gap:4px}
.site-footer .social span{width:11px;height:11px}
.copyright{height:22px;background:var(--navy);color:#dfe5ec;font-size:5px;text-align:center;line-height:22px}
</style>
</head>
<body>

<div class="guide">
  <div class="guide-logo"><div class="name">CALLOWAY</div><div class="sub">AERONAUTICS</div></div>
  <div class="guide-rule" style="left:517px"></div>
  <div class="guide-label" style="left:577px;top:158px">Fonts:</div>
  <div class="guide-font" style="top:202px">Tenor Sans</div>
  <div class="guide-font raleway" style="top:226px">Raleway</div>
  <div class="guide-rule" style="left:729px"></div>
  <div class="guide-label" style="left:788px;top:158px">Colors:</div>
  <div class="swatch" style="left:790px;background:#001c3b"></div>
  <div class="swatch" style="left:839px;background:#bdc8ce"></div>
  <div class="swatch" style="left:884px;background:#f7f7f7"></div>
  <div class="swatch-code" style="left:787px">#001c3b</div>
  <div class="swatch-code" style="left:836px">#bdc8ce</div>
  <div class="swatch-code" style="left:881px">#f7f7f7</div>
</div>

<div class="page">
  <div class="topbar">
    <div class="contact">
      <span><svg width="6" height="6" viewBox="0 0 10 10"><path d="M2 1l2 2-1 1.5c.6 1.2 1.4 2 2.5 2.5L7 6l2 2-1.2 1.5C4.5 9.2.8 5.5.5 2.2z" fill="#001c3b"/></svg>+1 555 435 7890</span>
      <span><svg width="7" height="5" viewBox="0 0 14 10"><rect width="14" height="10" fill="#001c3b"/><path d="M0 0l7 5 7-5" stroke="#bdc8ce" fill="none"/></svg>email@example.com</span>
    </div>
    <div class="social"><span></span><span></span><span></span></div>
  </div>

  <header class="nav">
    <div class="brand"><div class="name">CALLOWAY</div><div class="sub">AERONAUTICS</div></div>
    <nav class="menu"><span>HOME</span><span>ABOUT US</span><span>SERVICES</span><span>CONTACT</span></nav>
    <div class="call-btn">CALL US NOW</div>
  </header>

  <section class="hero">
    <div class="hero-photo" role="img" aria-label="Wide-body freighter jet nose and engine on the apron under a cloudy blue sky"></div>
    <div class="hero-box">
      <h1>WELCOME TO<br>CALLOWAY AERONAUTICS</h1>
      <p>We are an aviation company based in Bayview Shores, FL but with worldwide coverage. We are involved in commercial aircraft (mostly freighters) trading, sale &amp; leasing. Specifically, we specialized in freighters of the Vantrex family (V310, V320, V330, V340, V350).</p>
    </div>
    <div class="tagline"><p>Your Most Trusted and Professional Partner in the industry of Aviation</p></div>
  </section>

  <section class="about">
    <div class="eyebrow" style="left:142px;top:49px">INTRODUCTION</div>
    <h2 class="heading" style="left:142px;top:64px">About Us</h2>
    <p class="about-copy">Founded in 2011, Calloway Aeronautics' management has many years of experience in Aviation, a strong background in scheduled airlines with emphasis in all cargo operations, freight forwarding supply chain and freight logistics, as well as ACMI and CMI operations.</p>
    <div class="learn-btn">LEARN MORE</div>
    <div class="play"><svg width="7" height="8" viewBox="0 0 7 8"><path d="M0 0l7 4-7 4z" fill="#fff"/></svg></div>
    <div class="about-photo" role="img" aria-label="Smiling aviation executive in a suit standing beside an aircraft"></div>
    <div class="quote">
      <svg width="18" height="14" viewBox="0 0 18 14"><path d="M0 14V7C0 3 2 .5 6 0v3C4 3.5 3.5 5 3.5 7H7v7zm11 0V7c0-4 2-6.5 6-7v3c-2 .5-2.5 2-2.5 4H18v7z" fill="#fff"/></svg>
      <p>Calloway’s focuses in facilitating wet and dry lease operations, charter and ACMI programs consultancy, aircraft sales, leasing and procurement, aviation consultancy and aircraft management.</p>
    </div>
  </section>

  <section class="services">
    <div class="eyebrow center" style="top:46px">WHAT WE OFFER</div>
    <h2 class="heading center" style="top:64px">Services</h2>

    <div class="service" style="left:142px;top:103px"><div class="photo" role="img" aria-label="Business hands over documents with an airliner at sunset" style="background:linear-gradient(135deg,#e8d9b8,#b99a68 50%,#6d7f96)"></div><div class="label">Aircraft Finance <span class="dot-arrow"></span></div></div>
    <div class="service" style="left:293px;top:103px"><div class="photo" role="img" aria-label="Handshake in front of a jet aircraft" style="background:linear-gradient(180deg,#dfe3e8,#aab3bd 55%,#5a6470)"></div><div class="label active">Sale/Leaseback <span class="dot-arrow"></span></div></div>
    <div class="service" style="left:443px;top:103px"><div class="photo" role="img" aria-label="Freighter conversion inside a maintenance hangar" style="background:linear-gradient(180deg,#9fb3cc,#c9b884 55%,#6d7b8c)"></div><div class="label">Passenger to Freighter <span class="dot-arrow"></span></div></div>

    <div class="service" style="left:142px;top:239px"><div class="photo" role="img" aria-label="Jet engine and wing of a cargo aircraft on the ramp" style="background:linear-gradient(180deg,#dce3ec,#b9c4d1 50%,#7f8d9f)"></div><div class="label">Worldwide Charters <span class="dot-arrow"></span></div></div>
    <div class="service" style="left:293px;top:239px"><div class="photo" role="img" aria-label="Two consultants talking in an aircraft hangar" style="background:linear-gradient(180deg,#5d7fb0,#8aa1c1 50%,#3d4b62)"></div><div class="label">Aviation Consultancy <span class="dot-arrow"></span></div></div>
    <div class="service" style="left:443px;top:239px"><div class="photo" role="img" aria-label="Technician inspecting a turbofan engine" style="background:linear-gradient(135deg,#2c4f7e,#6687ad 50%,#e3b48f)"></div><div class="label">Aircraft Management <span class="dot-arrow"></span></div></div>

    <div class="all-link">Click Here To View All Services &nbsp;<span class="dot-arrow" style="width:6px;height:6px"></span></div>
  </section>

  <section class="stats">
    <div class="stat" style="left:136px"><b>178</b><span>Airlines we worked with</span></div>
    <div class="stat" style="left:247px"><b>6540</b><span>Satisfied Customers</span></div>
    <div class="stat" style="left:357px"><b>10</b><span>Years of experience</span></div>
    <div class="stat" style="left:468px"><b>23</b><span>Team of affirmed professionals</span></div>
  </section>

  <section class="faq">
    <div class="eyebrow center" style="top:46px">FAQS</div>
    <h2 class="heading center" style="top:64px">Frequently Asked Questions</h2>
    <div class="faq-col" style="left:142px">
      <div class="faq-q">Question Number One Goes Here? <i>–</i></div>
      <div class="faq-a">Lorem ipsum dolor sit amet, consectetur adipiscing elit. Ut elit tellus, luctus nec ullamcorper mattis, pulvinar dapibus leo.</div>
      <div class="faq-q">Question Number Two Goes Here? <i>+</i></div>
      <div class="faq-q">Question Number Three Goes Here? <i>+</i></div>
      <div class="faq-q">Question Number Four Goes Here? <i>+</i></div>
      <div class="faq-q">Question Number Five Goes Here? <i>+</i></div>
    </div>
    <div class="faq-col" style="left:372px">
      <div class="faq-q">Question Number One Goes Here? <i>–</i></div>
      <div class="faq-a">Lorem ipsum dolor sit amet, consectetur adipiscing elit. Ut elit tellus, luctus nec ullamcorper mattis, pulvinar dapibus leo.</div>
      <div class="faq-q">Question Number Two Goes Here? <i>+</i></div>
      <div class="faq-q">Question Number Three Goes Here? <i>+</i></div>
      <div class="faq-q">Question Number Four Goes Here? <i>+</i></div>
      <div class="faq-q">Question Number Five Goes Here? <i>+</i></div>
    </div>
  </section>

  <section class="banner">
    <svg class="cut" width="725" height="90" viewBox="0 0 725 90"><path d="M0 0H725V46L362 72 0 46z" fill="#fff"/></svg>
    <div class="plane" role="img" aria-label="Wide-body V350 freighter flying head-on toward the viewer"></div>
    <h2 class="center">CALLOWAY AERONAUTICS</h2>
    <p class="center">We also assist with financing, sale/leaseback. Handle special aviation projects and provide consultancy services.</p>
    <div class="quote-btn">REQUEST QUOTE</div>
  </section>

  <section class="filler">
    <h3>Text Filler</h3>
    <p>Lorem ipsum dolor sit amet, consectetur adipiscing elit, sed do eiusmod tempor incididunt ut labore et dolore magna aliqua. Ut enim ad minim veniam, quis nostrud exercitation ullamco laboris nisi ut aliquip ex ea commodo consequat.</p>
    <div class="ticks">
      <span><svg width="6" height="5" viewBox="0 0 6 5"><path d="M.5 2.5l1.8 1.8L5.5.6" stroke="#fff" fill="none"/></svg>Feature NO.1</span>
      <span><svg width="6" height="5" viewBox="0 0 6 5"><path d="M.5 2.5l1.8 1.8L5.5.6" stroke="#fff" fill="none"/></svg>Feature NO.2</span>
      <span><svg width="6" height="5" viewBox="0 0 6 5"><path d="M.5 2.5l1.8 1.8L5.5.6" stroke="#fff" fill="none"/></svg>Feature NO.3</span>
    </div>
    <div class="filler-photo" role="img" aria-label="White freighter aircraft parked before snowy mountains"></div>
  </section>

  <section class="testimonials">
    <div class="eyebrow center" style="top:46px">TESTIMONIALS</div>
    <h2 class="heading center" style="top:64px">What People Say</h2>
    <div class="arrow-nav" style="left:144px">‹</div>
    <div class="arrow-nav" style="left:573px">›</div>
    <div class="avatar" role="img" aria-label="Client portrait" style="left:242px"></div>
    <div class="avatar" role="img" aria-label="Client portrait" style="left:438px"></div>
    <div class="testi" style="left:175px">Lorem ipsum content. Lorem ipsum dolor sit amet, consectetur adipiscing elit. Ut elit tellus, luctus nec ullamcorper mattis, pulvinar dapibus leo.<b>OWEN PALMER</b><small>CEO</small></div>
    <div class="testi" style="left:371px">Lorem ipsum content. Lorem ipsum dolor sit amet, consectetur adipiscing elit. Ut elit tellus, luctus nec ullamcorper mattis, pulvinar dapibus leo.<b>LUCA FERRI</b><small>CEO</small></div>
    <div class="pager"><span></span><span class="on"></span></div>
  </section>

  <footer class="site-footer">
    <div class="foot-col" style="left:142px;width:210px">
      <h4>About</h4>
      <p>Lorem ipsum content. Lorem ipsum dolor sit amet, consectetur adipiscing elit. Ut elit tellus, luctus nec ullamcorper mattis pulvinar.</p>
    </div>
    <div class="foot-col" style="left:368px">
      <h4>Quick Links</h4>
      <ul><li>Home</li><li>About Us</li><li>Services</li><li>Contact</li></ul>
    </div>
    <div class="foot-col" style="left:500px">
      <h4>Information</h4>
      <ul><li>+1 555 435 7890</li><li>email@example.com</li><li>Bayview Shores, FL, United States</li></ul>
    </div>
    <div class="social"><span></span><span></span><span></span></div>
  </footer>
  <div class="copyright">Copyright 2021 © Calloway Aeronautics - All rights reserved</div>
</div>

</body>
</html>
```